New Human Resources Outsourcing company needs a brochure to explain services

I need a brochure that describes my business and the services we offer.

Everything we do is on my website as well. www.kelvorastaffing.com

Target Market(s)

Business Owners (Manufacturing, I.T. Financial Services)

Industry/Entity Type

Business

```html
<!DOCTYPE html>
<html lang="en">
<head>
<meta charset="utf-8">
<title>Kelvora Staffing – Benefits of Outsourcing Brochure</title>
<link rel="stylesheet" href="https://fonts.googleapis.com/css2?family=Questrial&family=Didact+Gothic&display=swap">
<style>
  :root {
    --stage: #d9d6d6;
    --paper: #ffffff;
    --purple-deep: #7b2fa8;
    --purple-mid: #a63fd0;
    --purple-bright: #c95af0;
    --teal-deep: #19b9ad;
    --teal-bright: #3fe8dc;
    --ink: #1c1c1c;
    --heading-ink: #3b3b3b;
    --white: #ffffff;
    --photo-light: #e6ebef;
    --photo-mid: #b8a79a;
    --photo-dark: #5a4a48;
  }
  html, body {
    margin: 0;
    width: 1200px;
    height: 900px;
    overflow: hidden;
    background: var(--stage);
  }
  .brochure {
    position: absolute;
    left: 178px;
    top: 147px;
    width: 842px;
    height: 594px;
    background: var(--paper);
    overflow: hidden;
    font-family: "Questrial", "Didact Gothic", sans-serif;
  }
  .brochure-art {
    position: absolute;
    inset: 0;
  }
  .panel-heading {
    position: absolute;
    margin: 0;
    font-family: "Questrial", sans-serif;
    font-weight: 700;
    font-size: 12.5px;
    color: var(--white);
    letter-spacing: 0.2px;
    padding-bottom: 3px;
    border-bottom: 1px solid rgba(255,255,255,0.55);
  }
  .panel-copy {
    position: absolute;
    margin: 0;
    font-size: 11.3px;
    line-height: 13.2px;
    text-align: justify;
    color: var(--white);
  }
  .panel-copy p { margin: 0 0 7px; }

  /* Left panel */
  .hr-pros-heading { left: 10px; top: 313px; width: 230px; }
  .hr-pros-copy { left: 10px; top: 336px; width: 261px; line-height: 12.2px; }
  .assist-heading {
    position: absolute;
    left: 10px;
    top: 428px;
    margin: 0;
    font-family: "Questrial", sans-serif;
    font-weight: 700;
    font-size: 12px;
    color: var(--white);
  }
  .service-list {
    position: absolute;
    left: 14px;
    top: 446px;
    margin: 0;
    padding: 0;
    list-style: none;
    font-size: 11px;
    line-height: 13.3px;
    color: var(--white);
  }
  .service-list li { display: flex; align-items: center; gap: 5px; }
  .service-list .tick { width: 9px; height: 9px; flex: none; }

  /* Middle panel */
  .benefits-title {
    position: absolute;
    right: 288px;
    top: 152px;
    margin: 0;
    text-align: right;
    font-family: "Questrial", sans-serif;
    font-weight: 400;
    color: var(--heading-ink);
    line-height: 1;
    white-space: nowrap;
  }
  .benefits-title .line-one { display: block; font-size: 35px; }
  .benefits-title .line-two { display: block; font-size: 21px; margin-top: 4px; }
  .benefits-rule {
    position: absolute;
    left: 388px;
    top: 218px;
    width: 166px;
    height: 1px;
    background: rgba(40,40,40,0.45);
  }
  .benefits-copy {
    left: 290px;
    top: 233px;
    width: 268px;
    color: var(--ink);
  }
  .benefits-copy strong { font-weight: 700; }

  /* Right panel */
  .owner-heading { left: 577px; top: 22px; width: 240px; }
  .owner-copy { left: 577px; top: 47px; width: 242px; }
  .owner-copy p { margin-bottom: 9px; }
</style>
</head>
<body>
<main class="brochure">
  <svg class="brochure-art" viewBox="0 0 842 594" width="842" height="594">
    <defs>
      <linearGradient id="purpleFill" x1="0" y1="0" x2="1" y2="0">
        <stop offset="0" stop-color="#7b2fa8"/>
        <stop offset="0.55" stop-color="#c95af0"/>
        <stop offset="1" stop-color="#a63fd0"/>
      </linearGradient>
      <linearGradient id="tealFill" x1="0" y1="0" x2="1" y2="1">
        <stop offset="0" stop-color="#19b9ad"/>
        <stop offset="0.5" stop-color="#3fe8dc"/>
        <stop offset="1" stop-color="#19b9ad"/>
      </linearGradient>
      <linearGradient id="meetingPhoto" x1="0" y1="0" x2="0" y2="1">
        <stop offset="0" stop-color="#e6ebef"/>
        <stop offset="0.5" stop-color="#b8a79a"/>
        <stop offset="1" stop-color="#5a4a48"/>
      </linearGradient>
      <linearGradient id="teamPhoto" x1="0" y1="0" x2="1" y2="0">
        <stop offset="0" stop-color="#9a8a7e"/>
        <stop offset="0.6" stop-color="#e9e6e4"/>
        <stop offset="1" stop-color="#c8c2c0"/>
      </linearGradient>
      <radialGradient id="celebratePhoto" cx="0.5" cy="0.5" r="0.6">
        <stop offset="0" stop-color="#e8eef4"/>
        <stop offset="1" stop-color="#a7b4c6"/>
      </radialGradient>
    </defs>

    <path d="M0,280 C110,290 230,272 300,205 L300,594 L0,594 Z" fill="#19b9ad"/>
    <path d="M0,298 C110,306 230,290 300,222 L300,594 L0,594 Z" fill="url(#purpleFill)"/>

    <path role="img" aria-label="Photo: business team meeting around a conference table"
          d="M0,0 H440 C410,80 350,190 240,238 C160,268 70,266 0,258 Z" fill="url(#meetingPhoto)"/>

    <path d="M440,0 H562 V594 H280 V300 C330,240 415,130 440,0 Z" fill="url(#tealFill)"/>

    <rect x="562" y="0" width="280" height="594" fill="url(#purpleFill)"/>
    <path d="M562,594 V468 C640,395 740,348 842,336 V594 Z" fill="#19b9ad"/>
    <path d="M562,594 V482 C640,410 740,362 842,350 V594 Z" fill="#eef0f2"/>
    <path role="img" aria-label="Photo: smiling team of young professionals"
          d="M530,594 L545,560 C600,450 730,385 842,372 V594 Z" fill="url(#teamPhoto)"/>

    <circle cx="212" cy="223" r="68" fill="#19b9ad"/>
    <circle cx="212" cy="223" r="64" fill="#ffffff"/>
    <circle role="img" aria-label="Photo: colleagues giving a high five" cx="212" cy="223" r="59" fill="url(#celebratePhoto)"/>
  </svg>

  <!-- Left panel -->
  <h2 class="panel-heading hr-pros-heading">Solutions For HR Professionals:</h2>
  <div class="panel-copy hr-pros-copy">
    <p>You’re an HR professional and you probably have a lot on your plate. That’s exactly why you need a good partner to help you minimize the frustrations of getting the HR job done. As your strategic partner, Kelvora Staffing will help you look good! Sometimes day to day stuff can get pretty hectic, that is why you need a partner.</p>
  </div>
  <h3 class="assist-heading">We can assist you with:</h3>
  <ul class="service-list">
    <li><svg class="tick" viewBox="0 0 9 9"><rect x="0.5" y="0.5" width="8" height="8" fill="none" stroke="#fff"/><path d="M2,4.5 L4,6.5 L7.5,2" fill="none" stroke="#fff" stroke-width="1.2"/></svg>Providing Administrative Assistance</li>
    <li><svg class="tick" viewBox="0 0 9 9"><rect x="0.5" y="0.5" width="8" height="8" fill="none" stroke="#fff"/><path d="M2,4.5 L4,6.5 L7.5,2" fill="none" stroke="#fff" stroke-width="1.2"/></svg>HR Compliance Assesments</li>
    <li><svg class="tick" viewBox="0 0 9 9"><rect x="0.5" y="0.5" width="8" height="8" fill="none" stroke="#fff"/><path d="M2,4.5 L4,6.5 L7.5,2" fill="none" stroke="#fff" stroke-width="1.2"/></svg>Performance Management</li>
    <li><svg class="tick" viewBox="0 0 9 9"><rect x="0.5" y="0.5" width="8" height="8" fill="none" stroke="#fff"/><path d="M2,4.5 L4,6.5 L7.5,2" fill="none" stroke="#fff" stroke-width="1.2"/></svg>Leadership Training</li>
    <li><svg class="tick" viewBox="0 0 9 9"><rect x="0.5" y="0.5" width="8" height="8" fill="none" stroke="#fff"/><path d="M2,4.5 L4,6.5 L7.5,2" fill="none" stroke="#fff" stroke-width="1.2"/></svg>Employee Handbooks</li>
    <li><svg class="tick" viewBox="0 0 9 9"><rect x="0.5" y="0.5" width="8" height="8" fill="none" stroke="#fff"/><path d="M2,4.5 L4,6.5 L7.5,2" fill="none" stroke="#fff" stroke-width="1.2"/></svg>Employee Investigations</li>
    <li><svg class="tick" viewBox="0 0 9 9"><rect x="0.5" y="0.5" width="8" height="8" fill="none" stroke="#fff"/><path d="M2,4.5 L4,6.5 L7.5,2" fill="none" stroke="#fff" stroke-width="1.2"/></svg>Onboarding and Separations</li>
    <li><svg class="tick" viewBox="0 0 9 9"><rect x="0.5" y="0.5" width="8" height="8" fill="none" stroke="#fff"/><path d="M2,4.5 L4,6.5 L7.5,2" fill="none" stroke="#fff" stroke-width="1.2"/></svg>Internal I-9 Audits</li>
    <li><svg class="tick" viewBox="0 0 9 9"><rect x="0.5" y="0.5" width="8" height="8" fill="none" stroke="#fff"/><path d="M2,4.5 L4,6.5 L7.5,2" fill="none" stroke="#fff" stroke-width="1.2"/></svg>Sexual Harassment Prevention Training</li>
    <li><svg class="tick" viewBox="0 0 9 9"><rect x="0.5" y="0.5" width="8" height="8" fill="none" stroke="#fff"/><path d="M2,4.5 L4,6.5 L7.5,2" fill="none" stroke="#fff" stroke-width="1.2"/></svg>Succession Planning</li>
  </ul>

  <!-- Middle panel -->
  <h1 class="benefits-title"><span class="line-one">Benefits of</span><span class="line-two">Outsourcing:</span></h1>
  <div class="benefits-rule"></div>
  <div class="panel-copy benefits-copy">
    <p><strong>Risk Management –</strong> Employment laws are complex and change often. It is difficult to keep up with the current legislation, while also focusing on running your business. Our HR Consultants understand best practices and can help make sure you avoid non-compliance and the resultant disputes and penalties.</p>
    <p><strong>Cost Savings -</strong> Outsourcing helps reduce the cost of maintaining nonrevenue-generating back-office expenses. A fully functional Human Resources department requires additional office space and highly trained and experienced HR staff.</p>
    <p><strong>Efficiency -</strong> Maintaining an efficient and productive workplace is critical. Outsourcing HR functions creates greater efficiency and helps employers spend less time doing paperwork and more time on growing their business.</p>
    <p style="text-align:left"><strong>Build a Competitive Advantage –</strong> Our HR Consultants are capable of developing training programs for all levels of employees and can assist you with performance management.</p>
  </div>

  <!-- Right panel -->
  <h2 class="panel-heading owner-heading">HR Solutions For The Business Owner:</h2>
  <div class="panel-copy owner-copy">
    <p>If you’re a business owner time is your most precious resource. Whether you are trying to grow your business or just survive the day to day, you are busy. Being pulled in so many different directions keeps you from giving your absolute full attention to anything, so pieces of your business or critical job functions fall through the cracks causing you even more stress.</p>
    <p>Knowing when to give up the reigns and let someone else take over a certain aspect of the business separates the extraordinary companies from the ordinary ones.</p>
    <p>That’s where Kelvora Staffing steps in. We offer proven HR Consulting &amp; HR Outsourcing solutions to help businesses upgrade the bottom line on human resources and improve employee issues management. We partner with you to provide workplace solutions to improve performance, reduce liability and increase profits so you can return to your first love...growing your business.</p>
  </div>
</main>
</body>
</html>
```